I am a Life Coaching and I have purchased the logo for my business. I need business cards

I need a business card design using the logo attached (but instead of the logo saying "Open Horizon Coaching" I need it to say "Open Horizon Coaching"

Target Market(s)

Middle-aged people

Industry/Entity Type

Life coaching

Contact Information for Business Card

Name, email address, phone number, website

Font styles to use
Serif
Sans Serif
Script

Colors
0094D4
00A9DD
6FCCEA
C7EBF8
E9F6FB
00AB8E
00BBA5
67D7C9
C6EFE9
E9F9F6
59FF00
82FF00
B8FF75
E3FFCB
F4FFEA

Requirements
Must have
• Logo and contact info above
Nice to have
• As close to the business card inspo attached as possible

```html
<!DOCTYPE html>
<html lang="en">
<head>
<meta charset="utf-8">
<title>Open Horizon Coaching – Business Cards</title>
<link rel="stylesheet" href="https://fonts.googleapis.com/css2?family=Arimo:wght@400;700&display=swap">
<style>
  :root {
    --page-bg: #e4e8eb;
    --card-white: #ffffff;
    --band-blue: #a9d8e6;
    --ornament-blue: #6fb7d0;
    --ornament-soft: #d3edf5;
    --ink: #111111;
    --icon-ring: #b5714f;
    --icon-fill: #4fa9cf;
  }
  * { margin: 0; padding: 0; box-sizing: border-box; }
  html, body {
    width: 1200px; height: 900px; overflow: hidden;
    background: var(--page-bg);
    font-family: "Arimo", Arial, sans-serif;
  }
  .sheet {
    position: relative; width: 1200px; height: 900px;
    display: flex; align-items: center; justify-content: center; gap: 60px;
  }
  .card {
    position: relative; width: 525px; height: 300px;
    background: var(--card-white);
    border-radius: 4px;
    overflow: hidden;
    box-shadow: 0 10px 28px rgba(0,0,0,0.18);
  }

  /* Contact side */
  .card-contact .ornament {
    position: absolute; left: -40px; top: 20px; width: 300px; height: 300px;
    border-radius: 50%;
    background: radial-gradient(circle at 30% 70%, var(--ornament-blue) 0%, var(--ornament-soft) 45%, rgba(255,255,255,0) 70%);
    opacity: 0.8;
  }
  .contact-block {
    position: absolute; left: 232px; top: 58px; width: 270px;
  }
  .person-name {
    font-weight: 700; font-size: 22px; letter-spacing: 0.5px; color: var(--ink);
    text-transform: uppercase; line-height: 1.1;
  }
  .person-role { font-size: 16px; color: var(--ink); margin-top: 4px; }
  .icon-row { display: flex; gap: 18px; margin: 16px 0 12px; }
  .icon-row svg { width: 28px; height: 28px; }
  .contact-lines { list-style: none; }
  .contact-lines li { font-size: 16px; color: var(--ink); line-height: 1.5; white-space: nowrap; }

  /* Logo side */
  .card-logo .band {
    position: absolute; left: 0; width: 100%; height: 58px;
    background: var(--band-blue);
  }
  .card-logo .band-top { top: 0; }
  .card-logo .band-bottom { bottom: 0; }
  .brand {
    position: absolute; inset: 58px 0; display: flex;
    align-items: center; justify-content: center; gap: 12px;
  }
  .brand-dot {
    flex: none; width: 24px; height: 24px; border-radius: 50%;
    border: 2px solid var(--ornament-blue);
  }
  .brand-name {
    font-size: 32px; font-weight: 400; color: var(--ink);
    letter-spacing: 0.5px; white-space: nowrap;
  }
</style>
</head>
<body>
<main class="sheet">

  <section class="card card-contact" aria-label="Business card, contact side">
    <div class="ornament" role="img" aria-label="Soft blue brushed floral decoration"></div>
    <div class="contact-block">
      <h1 class="person-name">Daniel Reyes</h1>
      <p class="person-role">Development Executive</p>
      <div class="icon-row">
        <svg viewBox="0 0 28 28" aria-label="Phone">
          <circle cx="14" cy="14" r="12.5" fill="none" stroke="var(--icon-ring)" stroke-width="1.5"/>
          <path d="M10 8.5c1-.6 1.8.2 2.3 1.3l.5 1.2c.3.7-.2 1.2-.7 1.6.5 1.5 1.6 2.7 3 3.4.4-.5.9-1 1.6-.7l1.3.5c1 .5 1.8 1.3 1.2 2.3-.8 1.2-2.2 1.6-3.6 1-3.2-1.3-5.5-3.7-6.6-6.8-.5-1.5 0-3 1-3.8z" fill="none" stroke="var(--icon-fill)" stroke-width="1.2"/>
        </svg>
        <svg viewBox="0 0 28 28" aria-label="Email">
          <circle cx="14" cy="14" r="12.5" fill="none" stroke="var(--icon-ring)" stroke-width="1.5"/>
          <rect x="7.5" y="9.5" width="13" height="9" fill="var(--icon-fill)"/>
          <path d="M7.5 9.5 14 15l6.5-5.5" fill="none" stroke="#fff" stroke-width="1"/>
        </svg>
        <svg viewBox="0 0 28 28" aria-label="Website">
          <circle cx="14" cy="14" r="12.5" fill="none" stroke="var(--icon-ring)" stroke-width="1.5"/>
          <circle cx="14" cy="14" r="6.5" fill="none" stroke="var(--icon-fill)" stroke-width="1.2"/>
          <ellipse cx="14" cy="14" rx="3" ry="6.5" fill="none" stroke="var(--icon-fill)" stroke-width="1"/>
          <path d="M7.5 14h13M8.5 10.8h11M8.5 17.2h11" stroke="var(--icon-fill)" stroke-width="1"/>
        </svg>
      </div>
      <ul class="contact-lines">
        <li>+789 555 0142</li>
        <li>hello@horizoncoach.com</li>
        <li>www.horizoncoach.com</li>
      </ul>
    </div>
  </section>

  <section class="card card-logo" aria-label="Business card, logo side">
    <div class="band band-top"></div>
    <div class="brand">
      <span class="brand-dot"></span>
      <span class="brand-name">Open Horizon Coaching</span>
    </div>
    <div class="band band-bottom"></div>
  </section>

</main>
</body>
</html>
```